Bench Advertisement - We Buy Houses Design Needed

Need a catchy, simple but elegant design for bus benches to advertise our company.

We need our website, or phone number, and a smal description (1-2 bulletpoints of what we do and what we offer)

The tricky part is for the designer to fit everything and make the website name as part of the title and fitting everything so that people passing by on the street can see what we offer.

Our website is quickhomebuyerdesk.com - (916) 482-3091

Something simple but something that catches the eye of walking pedestrians, and drivers driving by the bench.

Our company buys houses, any condition, any situation, we buy houses for cash and close quickly. You can use this description to create a few bulletpoints however you like. Must follow dimensions in attachment.

Target Market(s)

People in foreclosure, about to lose their homes, people that need a quick cash sale of their property

Industry/Entity Type

Real Estate

Requirements
Must have
• catchy, website name, phone number, few brief bulletpoints about what we offer, colors that will catch peoples eye while walking or driving - advertisement will be placed on bus benches - visit our website to see the type of houses we buy - Also have more work for winner of design with possible bonuses
Nice to have
• Feel free to use description or images on our website - make sure the description is just bullet points and it fits with the overall theme / size of the advertisement - Bold bright colors - put yourself in their shoes (if you were going through financial difficulties and about to lose your house to foreclosure or auction, what would you want to see to pick up the phone and call us for a quick sale of your house?) (or if you have a house that you are having a problem with, problem renters, unkept/beat up house, what would make you want to call us and sell your house to us?)

```html
<!DOCTYPE html>
<html lang="en">
<head>
<meta charset="utf-8">
<title>Quick Home Buyer Desk – Bench Advertisement</title>
<link href="https://fonts.googleapis.com/css2?family=Fira+Sans+Condensed:wght@600;700&family=PT+Sans:wght@400;700&display=swap" rel="stylesheet">
<style>
  :root{
    --page:#ffffff;
    --frame:#e6e6e6;
    --blue:#0063a8;
    --yellow:#fff200;
    --white:#ffffff;
    --red:#e3221b;
    --navy:#0b5aa6;
    --rule:#e08a2a;
  }
  html,body{margin:0;padding:0;overflow:hidden;}
  body{width:1200px;height:1200px;background:var(--page);position:relative;}
  .canvas-edge{position:absolute;inset:0;border:1px solid #cfcfcf;box-sizing:border-box;}
  .bench-ad{position:absolute;left:60px;width:1108px;height:315px;border:1px solid var(--frame);box-sizing:border-box;}
  .bench-ad.top{top:246px;}
  .bench-ad.bottom{top:778px;}
  .panel{position:absolute;left:12px;top:13px;width:1084px;height:247px;background:var(--blue);}
  .brand{position:absolute;left:0;width:394px;top:154px;text-align:center;
    font-family:"PT Sans",sans-serif;font-weight:400;font-size:22px;letter-spacing:.5px;color:var(--white);}
  .brand-mark{display:block;width:26px;height:26px;background:var(--white);margin:0 auto 14px;}
  .website{position:absolute;left:378px;top:76px;display:flex;align-items:center;gap:8px;
    font-family:"PT Sans",sans-serif;font-weight:700;font-size:38px;color:var(--white);}
  .phone{position:absolute;left:444px;top:134px;display:flex;align-items:center;gap:18px;
    font-family:"Fira Sans Condensed",sans-serif;font-weight:700;font-size:74px;color:var(--yellow);line-height:1;}
  .offer-band{position:absolute;left:12px;top:260px;width:1084px;height:42px;background:var(--yellow);}
  .offer-band span{position:absolute;top:0;line-height:42px;white-space:nowrap;font-family:"Fira Sans Condensed",sans-serif;font-weight:700;}
  .call-label{left:32px;font-size:26px;color:var(--navy);}
  .offer{font-size:19px;color:var(--red);}
  .offer svg{position:absolute;left:-22px;top:12px;}
  .offer::before{content:"";position:absolute;left:-14px;top:4px;height:34px;border-left:1px dashed var(--rule);}
</style>
</head>
<body>
<div class="canvas-edge"></div>

<section class="bench-ad top">
  <div class="panel">
    <div class="brand"><span class="brand-mark"></span>QUICK HOME BUYER DESK</div>
    <div class="website">
      <svg width="34" height="34" viewBox="0 0 34 34" aria-hidden="true">
        <g fill="none" stroke="var(--yellow)" stroke-width="2">
          <circle cx="17" cy="17" r="15"/><ellipse cx="17" cy="17" rx="7" ry="15"/>
          <line x1="2" y1="17" x2="32" y2="17"/><line x1="17" y1="2" x2="17" y2="32"/>
          <path d="M5 9h24M5 25h24"/>
        </g>
      </svg>
      www.quickhomebuyerdesk.com
    </div>
    <div class="phone">
      <svg width="54" height="54" viewBox="0 0 54 54" aria-hidden="true">
        <circle cx="27" cy="27" r="27" fill="var(--yellow)"/>
        <path d="M20 12c3-1 5 5 5 7s-3 2-3 4c0 4 5 11 8 12 2 0 2-3 4-3s7 3 6 6-4 5-7 4C22 40 14 26 14 19c0-3 3-6 6-7z" fill="var(--red)"/>
      </svg>
      (916) 482-3091
    </div>
  </div>
  <div class="offer-band">
    <span class="call-label">CALL US :</span>
    <span class="offer" style="left:168px"><svg width="14" height="14" viewBox="0 0 14 14"><path d="M7 0L14 7H11V14H3V7H0z" fill="var(--navy)"/></svg>Financial Difficulties</span>
    <span class="offer" style="left:364px"><svg width="14" height="14" viewBox="0 0 14 14"><path d="M7 0L14 7H11V14H3V7H0z" fill="var(--navy)"/></svg>Foreclosure or Auction</span>
    <span class="offer" style="left:582px"><svg width="14" height="14" viewBox="0 0 14 14"><path d="M7 0L14 7H11V14H3V7H0z" fill="var(--navy)"/></svg>Quick Sale</span>
    <span class="offer" style="left:697px"><svg width="14" height="14" viewBox="0 0 14 14"><path d="M7 0L14 7H11V14H3V7H0z" fill="var(--navy)"/></svg>Problem Renters</span>
    <span class="offer" style="left:869px"><svg width="14" height="14" viewBox="0 0 14 14"><path d="M7 0L14 7H11V14H3V7H0z" fill="var(--navy)"/></svg>Unkept / beat uo House</span>
  </div>
</section>

<section class="bench-ad bottom">
  <div class="panel">
    <div class="brand"><span class="brand-mark"></span>QUICK HOME BUYER DESK</div>
    <div class="website">
      <svg width="34" height="34" viewBox="0 0 34 34" aria-hidden="true">
        <g fill="none" stroke="var(--yellow)" stroke-width="2">
          <circle cx="17" cy="17" r="15"/><ellipse cx="17" cy="17" rx="7" ry="15"/>
          <line x1="2" y1="17" x2="32" y2="17"/><line x1="17" y1="2" x2="17" y2="32"/>
          <path d="M5 9h24M5 25h24"/>
        </g>
      </svg>
      www.quickhomebuyerdesk.com
    </div>
    <div class="phone">
      <svg width="54" height="54" viewBox="0 0 54 54" aria-hidden="true">
        <circle cx="27" cy="27" r="27" fill="var(--yellow)"/>
        <path d="M20 12c3-1 5 5 5 7s-3 2-3 4c0 4 5 11 8 12 2 0 2-3 4-3s7 3 6 6-4 5-7 4C22 40 14 26 14 19c0-3 3-6 6-7z" fill="var(--red)"/>
      </svg>
      (916) 482-3091
    </div>
  </div>
  <div class="offer-band">
    <span class="call-label">CALL US :</span>
    <span class="offer" style="left:168px"><svg width="14" height="14" viewBox="0 0 14 14"><path d="M7 0L14 7H11V14H3V7H0z" fill="var(--navy)"/></svg>Financial Difficulties</span>
    <span class="offer" style="left:364px"><svg width="14" height="14" viewBox="0 0 14 14"><path d="M7 0L14 7H11V14H3V7H0z" fill="var(--navy)"/></svg>Foreclosure or Auction</span>
    <span class="offer" style="left:582px"><svg width="14" height="14" viewBox="0 0 14 14"><path d="M7 0L14 7H11V14H3V7H0z" fill="var(--navy)"/></svg>Quick Sale</span>
    <span class="offer" style="left:697px"><svg width="14" height="14" viewBox="0 0 14 14"><path d="M7 0L14 7H11V14H3V7H0z" fill="var(--navy)"/></svg>Problem Renters</span>
    <span class="offer" style="left:869px"><svg width="14" height="14" viewBox="0 0 14 14"><path d="M7 0L14 7H11V14H3V7H0z" fill="var(--navy)"/></svg>Unkept / beat uo House</span>
  </div>
</section>
</body>
</html>
```